Business Card Design - Brightfold Dwellings

Hi there,

We would like a business card for our new venture, Brightfold Dwellings.

We are based in Western Australia and specialise in taking tired, old properties and making them look new again. We aim to create enjoyably liveable homes for young families in particular.

Product pricing is mid range i.e. appliances, furnishings, fixtures (not top end but not cheap either)

Our work is primarily cosmetic renovation (approx. 80%) and the rest construction (approx 20%).

We would like a business card that conveys the following:
- clean, simplistic/minimalistic design
- modern, contemporary style
- a touch of funk/uniqueness
- appealing to both females and males
- professionalism

I have uploaded our logo in grey or green, I do not mind which one you choose to use (please use either coloured logo on the pure white background not the white on colour version).

Details to include on the business card are:
Names: Corina Maddox and Pete Okonbrie
Mobile: 0417 362 908
Email: info@brightfolddwellings.com.au
Website: www.brightfolddwellings.com.au (note: this website is currently being developed)
Note: We will provide final details such as mobile number and names on on selection of successful design)

On the other side of the card please include a line similar to "We buy tired, un-renovated properties and sell them looking new again!"

The business card will also need to include the following "ABN 47 219 635 104" which is our Australian Business Number (again the actual number will be provided on selection of successful design). We would like this number somewhere near our name Brightfold Dwellings but in much smaller text.

The purpose of the business cards will be to give to suppliers, real estate agents, people wanting assistance in locating a property in need of renovation and potential buyers.

Thank you and please let me know if you have any further questions.

```html
<!DOCTYPE html>
<html lang="en">
<head>
<meta charset="utf-8">
<title>Brightfold Dwellings – Business Card</title>
<link rel="stylesheet" href="https://fonts.googleapis.com/css2?family=Open+Sans:wght@400;600&display=swap">
<style>
  :root {
    --leaf: #a8cd45;
    --charcoal: #333333;
    --paper: #ffffff;
    --sheet: #ffffff;
    --rule: #555555;
    --label: #333333;
  }
  * { box-sizing: border-box; margin: 0; padding: 0; }
  html, body { width: 1200px; height: 441px; overflow: hidden; background: var(--sheet); }
  body { font-family: "Open Sans", Arial, sans-serif; color: var(--charcoal); }

  .presentation {
    position: relative;
    width: 1200px;
    height: 441px;
    border: 1px solid var(--rule);
  }

  .card {
    position: absolute;
    top: 52px;
    width: 507px;
    height: 309px;
    background: var(--paper);
    border: 1px solid var(--rule);
    overflow: hidden;
  }
  .card--front { left: 45px; }
  .card--back { left: 650px; }

  .side-label {
    position: absolute;
    top: 376px;
    width: 507px;
    text-align: center;
    font-size: 24px;
    color: var(--label);
  }
  .side-label--front { left: 45px; }
  .side-label--back { left: 650px; }

  /* Front */
  .brand {
    position: absolute;
    left: 0;
    top: 150px;
    width: 100%;
    display: flex;
    justify-content: center;
    align-items: center;
    gap: 12px;
  }
  .brand__dot {
    width: 22px;
    height: 22px;
    border-radius: 50%;
    background: var(--leaf);
  }
  .brand__name {
    font-size: 38px;
    font-weight: 400;
    color: var(--leaf);
    letter-spacing: -0.5px;
    line-height: 1;
  }
  .tagline {
    position: absolute;
    left: 65px;
    top: 221px;
    width: 374px;
    height: 19px;
    background: var(--leaf);
    color: var(--paper);
    font-size: 10.5px;
    line-height: 19px;
    text-align: center;
  }

  /* Back */
  .abn {
    position: absolute;
    right: 28px;
    top: 32px;
    font-size: 9.5px;
    letter-spacing: 0.3px;
    color: var(--charcoal);
  }
  .holder-name {
    position: absolute;
    left: 36px;
    top: 64px;
    font-size: 17px;
    font-weight: 600;
    color: var(--charcoal);
  }
  .contact-band {
    position: absolute;
    left: 0;
    top: 208px;
    width: 283px;
    height: 72px;
    background: var(--leaf);
    padding: 6px 0 0 36px;
    list-style: none;
  }
  .contact-band li {
    color: var(--paper);
    font-size: 12.5px;
    line-height: 24px;
    white-space: nowrap;
  }
  .address {
    position: absolute;
    right: 28px;
    top: 232px;
    text-align: right;
    font-size: 13.5px;
    line-height: 18px;
    color: var(--charcoal);
  }
</style>
</head>
<body>
  <main class="presentation">
    <section class="card card--front" aria-label="Card front">
      <div class="brand">
        <span class="brand__dot" aria-hidden="true"></span>
        <span class="brand__name">Brightfold Dwellings</span>
      </div>
      <p class="tagline">We buy tired, un-renovated properties and sell them looking new again!</p>
    </section>
    <p class="side-label side-label--front">Front</p>

    <section class="card card--back" aria-label="Card back">
      <p class="abn">ABN 47 219 635 104</p>
      <h1 class="holder-name">Corina Maddox</h1>
      <ul class="contact-band">
        <li>M: 0417 362 908</li>
        <li>E: info@brightfolddwellings.com.au</li>
        <li>W: www.brightfolddwellings.com.au</li>
      </ul>
      <address class="address" style="font-style: normal;">H:No 123, Street Name,<br>City Name -000000</address>
    </section>
    <p class="side-label side-label--back">Back</p>
  </main>
</body>
</html>
```